Drifting Pelican Coffee Co menu

We would like our existing menu tidied up.
we want to keep the all the items, but need it less busy and clearer to read.

Also want to leave a bit of space to add a few item in the future.

```html
<!DOCTYPE html>
<html lang="en">
<head>
<meta charset="utf-8">
<title>Drifting Pelican Coffee Co – Menu</title>
<link href="https://fonts.googleapis.com/css2?family=Arimo:wght@400;700&family=Sancreek&display=swap" rel="stylesheet">
<style>
:root{
  --backdrop:#6b6b6f;
  --paper:#ffffff;
  --ink:#1c1a1b;
  --panel:#242122;
  --rule:#2a2a2a;
  --leader:#777;
  --photo-a:#e9edf1;
  --photo-b:#8d9aa6;
  --photo-c:#3b3f44;
}
*{margin:0;padding:0;box-sizing:border-box}
html,body{width:1200px;height:547px;overflow:hidden;background:var(--backdrop)}
body{position:relative;font-family:"Arimo",Arial,sans-serif;color:var(--ink)}
.page{position:absolute;top:25px;width:650px;height:920px;background:var(--paper);transform:scale(.54);transform-origin:0 0;overflow:hidden}
.page--coffee{left:237px}
.page--iced{left:612px}
.frame{position:absolute;left:26px;top:30px;right:26px;bottom:26px;border:1.5px solid var(--rule);border-radius:14px}
.display{font-family:"Sancreek",serif;font-weight:400;text-align:center;color:var(--ink);letter-spacing:.5px}
.rule{position:absolute;height:1.5px;background:var(--rule)}
.bar{position:absolute;height:24px;background:var(--ink);color:#fff;font-weight:700;font-size:19px;line-height:24px;padding-left:12px;border-radius:0 4px 4px 0;letter-spacing:.3px}
/* header */
.brand{position:absolute;left:50px;top:60px;width:250px;height:110px;display:flex;align-items:center;justify-content:center;text-align:center;font-weight:700;font-size:24px;line-height:1.1}
.photo{position:absolute;left:300px;top:52px;width:306px;height:123px;background:linear-gradient(100deg,var(--photo-a) 0%,var(--photo-b) 55%,var(--photo-c) 100%);border-radius:0 0 22px 0}
.photo__url{position:absolute;right:38px;top:12px;color:#fff;font-size:12.5px;letter-spacing:.5px}
/* price tables */
.col{position:absolute}
.sizes{display:grid;grid-template-columns:56px 58px 44px;justify-content:end;font-weight:700;font-size:10.5px;text-align:right;padding-right:4px;margin-bottom:2px}
.sizes--tea{grid-template-columns:52px 58px 46px}
.item{position:relative;border-bottom:1px dashed var(--leader);padding:3px 0}
.item p{white-space:nowrap;font-size:10.5px;line-height:13px}
.item b{display:block;font-size:12.5px;line-height:15px}
.item--tea{padding-top:10px}
.prices{position:absolute;right:4px;bottom:3px;display:grid;grid-template-columns:56px 58px 44px;text-align:right;font-size:10.5px;line-height:13px}
.item--tea .prices{grid-template-columns:52px 58px 46px}
.item--last{border-bottom:none}
.addon{font-size:10.5px;margin-top:12px;line-height:1.3}
.addon b{font-size:12.5px}
.addon .lead{display:flex;align-items:baseline;gap:4px}
.addon .lead i{flex:1;border-bottom:1px dashed var(--leader)}
/* list with leaders */
.list{list-style:none}
.list li{display:flex;align-items:baseline;gap:8px;font-weight:700;font-size:12.5px;margin-bottom:17px}
.list li i{flex:1;border-bottom:1px dashed var(--leader);transform:translateY(-3px)}
.list li small{display:block;font-weight:400;font-size:10.5px;margin-top:2px}
.list .lead{display:flex;gap:8px;align-items:baseline}
.list .lead i{flex:1;border-bottom:1px dashed var(--leader)}
.note{font-size:10.5px;line-height:1.2;margin-bottom:14px}
/* macchiato */
.mac{font-size:10.5px;line-height:1.3;margin-bottom:12px}
.mac .lead{display:flex;align-items:baseline;gap:6px;font-weight:700;font-size:12.5px}
.mac .lead i{flex:1;border-bottom:1px dashed var(--leader)}
.mac .lead em{font-style:normal;font-size:10.5px}
/* specialty */
.special{position:absolute;background:var(--panel);color:#fff;border-radius:28px 28px 8px 8px;padding:20px 18px 0;display:grid;grid-template-columns:222px 1fr;column-gap:24px}
.special__tab{position:absolute;left:50%;top:-14px;transform:translateX(-50%);background:#fff;color:var(--ink);border:1.5px solid var(--ink);border-bottom:none;border-radius:8px 8px 0 0;padding:1px 16px;font-weight:700;font-size:19px;letter-spacing:.3px;white-space:nowrap}
.drink{font-size:9.5px;line-height:12.8px;margin-bottom:9px}
.drink h4{font-size:12px;line-height:15px;margin-bottom:3px;display:flex;gap:5px;align-items:baseline;white-space:nowrap}
.drink h4 i{flex:0 0 22px;border-bottom:1px dashed #ccc}
.drink h4.stack{display:block}
</style>
</head>
<body>

<section class="page page--coffee">
  <div class="frame"></div>
  <div class="brand">Drifting Pelican<br>Coffee Co</div>
  <div class="photo" role="img" aria-label="Photo of an espresso pouring into a cup with steam">
    <span class="photo__url">www.driftingpelican.com.au</span>
  </div>
  <div class="rule" style="left:45px;top:188px;width:560px"></div>
  <h1 class="display" style="position:absolute;left:0;right:0;top:190px;font-size:42px">COFFEE &amp; TEA</h1>
  <div class="rule" style="left:45px;top:238px;width:560px"></div>

  <div class="bar" style="left:45px;top:251px;width:246px">COFFEE</div>
  <div class="bar" style="left:345px;top:251px;width:262px">TEA / OTHER DRINKS</div>

  <div class="col" style="left:45px;top:290px;width:280px">
    <div class="sizes"><span>Small</span><span>Medium</span><span>Large</span></div>
    <div class="item"><p><b>FLAT WHITE</b>Espresso shot with<br>a steamed milk</p><div class="prices"><span>$5</span><span>$6</span><span>$7</span></div></div>
    <div class="item"><p><b>CAPPUCCINO</b>Espresso shot with steamed milk,<br>a thick layer of milk foam and<br>chocolate powder topping</p><div class="prices"><span>$5</span><span>$6</span><span>$7</span></div></div>
    <div class="item"><p><b>LATTE</b>Espresso shot with steamed<br>milk and a thin layer of<br>milk foam</p><div class="prices"><span>$5</span><span>$6</span><span>$7</span></div></div>
    <div class="item"><p><b>MOCHA</b>Espresso shot, Belgian<br>chocolate RAW natural<br>infusion with a medium layer<br>of milk foam.</p><div class="prices"><span>$5</span><span>$6</span><span>$7</span></div></div>
    <div class="item"><p><b>AMERICANO</b>Americano - Espresso shot<br>topped up with hot water.<br>Long Black - Hot water topped<br>off with espresso shot</p><div class="prices"><span>$5</span><span>$6</span><span>$7</span></div></div>
    <div class="item"><p><b>ESPRESSO</b>Double espresso shot</p><div class="prices"><span>$5</span><span>$6</span><span>$7</span></div></div>
    <div class="item item--last"><p><b>FILTER /<br>BATCH BREW COFFEE</b></p><div class="prices" style="bottom:4px"><span>$5</span><span>$6</span><span>$7</span></div></div>
  </div>

  <div class="col" style="left:345px;top:290px;width:262px">
    <div class="sizes sizes--tea"><span>Small</span><span>Medium</span><span>Large</span></div>
    <div class="item item--tea"><p><b>ORGANIC<br>GREEN TEA</b></p><div class="prices"><span>$5</span><span>$6</span><span>$7</span></div></div>
    <div class="item item--tea"><p><b>ENGLISH<br>BREAKFAST TEA</b></p><div class="prices"><span>$5</span><span>$6</span><span>$7</span></div></div>
    <div class="item item--tea"><p><b>ORGANIC EARL<br>GREY TEA</b></p><div class="prices"><span>$5</span><span>$6</span><span>$7</span></div></div>
    <div class="item item--tea"><p><b>HOT<br>CHOCOLATE</b></p><div class="prices"><span>$5</span><span>$6</span><span>$7</span></div></div>
    <div class="item item--tea"><p><b>DARK CACOA<br>HOT CHOCOLATE</b></p><div class="prices"><span>$5</span><span>$6</span><span>$7</span></div></div>
    <div class="item item--tea"><p><b>CHAI LATTE</b></p><div class="prices"><span>$5</span><span>$6</span><span>$7</span></div></div>
    <div class="addon"><div class="lead"><b>RAW Natural Infusions</b><i></i>$0.50</div>CARAMEL, VANILLA, CHAI SPICE,<br>HAZELNUT, BELGIAN CHOCOLATE</div>
    <div class="addon"><div class="lead"><b>MILKS</b><i></i>$INC</div>FULL CREAM, SKINNY, OAT,<br>ALMOND, SOY</div>
  </div>
  <div class="rule" style="left:345px;top:693px;width:262px;height:1px"></div>

  <div class="special" style="left:45px;top:742px;width:560px;height:138px">
    <div class="special__tab">SPECIALTY DRINKS</div>
    <div class="drink"><h4>HONEY BREWED CHAI<i></i>$7.00</h4>Our Honey Chai is handmade and blended in Western Australia. It is made from the finest black tea leaves available, aromatic freshly ground spices and infused with locally sourced raw honey. Served with a choice of steamed milk.</div>
    <div class="drink"><h4 class="stack">COLOMBIAN CACOA SALTED CARAMEL<br>HOT CHOCOLATE &nbsp;_ _ _ $7.00</h4>Made with deep toned and rich cocoa sourced from ancient cocao growing regions of Colombia and sweetened with just enough organic unrefined Colombian panela, all balanced perfectly with a caramel RAW natural infusion and pink Himalayan rock salt. Served with a choice of steamed milk.</div>
  </div>
</section>

<section class="page page--iced">
  <div class="frame"></div>
  <h1 class="display" style="position:absolute;left:0;right:0;top:44px;font-size:40px">ICED COFFEE &amp; MILKSHAKES</h1>
  <div class="rule" style="left:45px;top:94px;width:562px"></div>

  <div class="bar" style="left:45px;top:110px;width:246px">ICED COFFEE</div>
  <div class="bar" style="left:345px;top:110px;width:262px">MILKSHAKES</div>

  <ul class="list col" style="left:45px;top:150px;width:247px">
    <li style="display:block"><span class="lead">ICED LATTE<i></i>$7.50</span><small>Add icecream + $1.00</small></li>
    <li>ICED MOCHA<i></i>$8.00</li>
    <li>ICED AMERICANO<i></i>$6.00</li>
    <li>COLD BREW<i></i>$7.50</li>
  </ul>

  <div class="bar" style="left:45px;top:312px;width:246px">OTHER DRINKS</div>
  <ul class="list col" style="left:45px;top:351px;width:247px">
    <li>ICED CHOCOLATE<i></i>$7.00</li>
    <li>ICED CHAI<i></i>$7.00</li>
    <li>PUPPYCINO<i></i>$2.00</li>
  </ul>

  <div class="col" style="left:345px;top:151px;width:262px">
    <p class="note">Milkshake with a choice of chilled milk<br>and ice cream.</p>
    <ul class="list">
      <li>CHOCOLATE<i></i>$8.00</li>
      <li>VANILLA<i></i>$8.00</li>
      <li>CARAMEL<i></i>$8.00</li>
      <li>STRAWBERRY<i></i>$8.00</li>
      <li>MANGO<i></i>$8.00</li>
      <li>BANANA<i></i>$8.00</li>
      <li>COOKIES &amp; CREAM<i></i>$8.00</li>
      <li>HAZELNOVA MILKSHAKE<i></i>$9.00</li>
    </ul>
  </div>

  <div class="rule" style="left:45px;top:454px;width:562px"></div>
  <h2 class="display" style="position:absolute;left:0;right:0;top:456px;font-size:40px">MACCHIATO MENU</h2>
  <div class="rule" style="left:45px;top:503px;width:562px"></div>

  <div class="col" style="left:45px;top:520px;width:272px">
    <div class="mac"><div class="lead">MACCHIATO <em>(TRADITIONAL)</em><i></i>$5.00</div>Traditional Macchiato coming from the Italian<br>word for “stain”. A small stain of milk foam on<br>a double espresso.</div>
    <div class="mac"><div class="lead">LONG MACCHIATO <em>(TRADITIONAL)</em><i></i>$5.00</div>Long Macchiato adding volume to the drink<br>with 50/50 milk espresso ratio.</div>
  </div>
  <div class="col" style="left:339px;top:520px;width:268px">
    <div class="mac"><div class="lead">LONG MACCHIATO <em>(MODERN)</em><i></i>$5.00</div>Long Macchiato adding volume to the drink<br>with 50/50 water espresso ratio.</div>
    <div class="mac"><div class="lead">LONG MACCHIATO TOPPED UP*<i></i>$5.50</div>A Perth based colloquilist for a latte with<br>extra shot. Can be 3/4 or fully topped up.</div>
  </div>

  <div class="special" style="left:45px;top:660px;width:562px;height:220px">
    <div class="special__tab">SPECIALTY DRINKS</div>
    <div>
      <div class="drink"><h4>CRUMBLEBERRY ICED COFFEE<i style="flex-basis:8px"></i>$9.00</h4>A double shot of espresso extracted over<br>Crumbleberry spread poured over Greenvale<br>premium extra creamy milk and ice cream<br>Topped off with whipped cream and<br>crushed Crumbleberry cookies.</div>
      <div class="drink"><h4>MALTIPOPS ICED COFFEE<i style="flex-basis:14px"></i>$9.00</h4>A double shot of espresso extracted over<br>melted Maltipops Poured over Greenvale<br>premium extra creamy milk and ice cream<br>Topped off with whipped cream and more<br>crushed Maltipops.</div>
    </div>
    <div>
      <div class="drink"><h4>HAZELNOVA ICED COFFEE<i></i>$9.00</h4>A double shot of espresso extracted over melted Hazelnova Poured over Greenvale premium extra creamy milk and ice cream Topped off with whipped cream and more Hazelnova sauce and crushed Hazelnuts.</div>
      <div class="drink"><h4 class="stack">COLOMBIAN CACOA &nbsp;_ _ _ _ _ &nbsp;$9.00<br>SALTED CARAMEL MILKSHAKE</h4>Made with deep toned and rich cocoa sourced from ancient cocao growing regions of Colombia and sweetened with just enough organic unrefined Colombian panela, all balanced perfectly with a caramel RAW natural infusion and pink Himalayan rock salt. All blended together with icecream and a choice of milk.</div>
    </div>
  </div>
</section>

</body>
</html>
```